Copperleaf Motorized Shade Business Card

Hello, we've had our logo made. Now we are looking for a clean and cool looking business card. One side can just be the logo with any design elements that might look good with it. The other side will be Name, Phone Number and Email. There will not be an address on the card.

```html
<!DOCTYPE html>
<html lang="en">
<head>
<meta charset="utf-8">
<title>Copperleaf Motorized Shade Business Card</title>
<link href="https://fonts.googleapis.com/css2?family=Montserrat:wght@500;700&display=swap" rel="stylesheet">
<style>
  :root {
    --navy: #17427a;
    --sun: #f2b51c;
    --paper: #f3f3f3;
    --stage: #2f2f2f;
    --white: #ffffff;
  }
  * { margin: 0; padding: 0; box-sizing: border-box; }
  html, body { width: 1200px; height: 800px; overflow: hidden; }
  body {
    background: var(--stage);
    font-family: "Montserrat", sans-serif;
    display: flex;
    align-items: center;
    justify-content: center;
    gap: 60px;
  }
  .card {
    position: relative;
    width: 520px;
    height: 297px;
    border-radius: 3px;
    overflow: hidden;
    box-shadow: 0 18px 30px rgba(0,0,0,0.45);
  }
  .card--front { background: var(--navy); }
  .card--back { background: var(--paper); }
  .card__wave { position: absolute; inset: 0; width: 100%; height: 100%; }

  .brand {
    position: absolute;
    display: flex;
    align-items: center;
    gap: 12px;
  }
  .card--front .brand { left: 50%; top: 50%; transform: translate(-50%, -50%); }
  .card--back .brand { left: 50%; top: 29%; transform: translate(-50%, -50%); }
  .brand__dot {
    width: 26px; height: 26px; border-radius: 50%;
    background: var(--sun); flex: none;
  }
  .brand__name {
    font-weight: 700;
    font-size: 26px;
    line-height: 1.1;
    letter-spacing: 0.5px;
    text-transform: uppercase;
  }
  .card--front .brand__name { color: var(--white); }
  .card--back .brand__name { color: var(--navy); }

  .holder {
    position: absolute;
    left: 34px; bottom: 30px;
    color: var(--white);
    font-weight: 500;
    font-size: 17px;
    letter-spacing: 0.5px;
  }
  .contact {
    position: absolute;
    right: 30px; bottom: 22px;
    color: var(--white);
    text-align: left;
    font-weight: 500;
    line-height: 1.45;
  }
  .contact__phone { font-size: 16px; font-weight: 700; letter-spacing: 0.5px; }
  .contact__email { font-size: 14px; }
</style>
</head>
<body>
  <section class="card card--front" aria-label="Card front">
    <div class="brand">
      <span class="brand__dot"></span>
      <span class="brand__name">Copperleaf<br>Motorized Shades</span>
    </div>
  </section>

  <section class="card card--back" aria-label="Card back">
    <svg class="card__wave" viewBox="0 0 520 297" preserveAspectRatio="none" aria-hidden="true">
      <path d="M0 100 C 80 180, 260 210, 520 190 L520 297 L0 297 Z" fill="#f2b51c"/>
      <path d="M0 112 C 80 192, 260 222, 520 202 L520 297 L0 297 Z" fill="#17427a"/>
    </svg>
    <div class="brand">
      <span class="brand__dot"></span>
      <span class="brand__name">Copperleaf<br>Motorized Shades</span>
    </div>
    <p class="holder">ABC WXYZ</p>
    <div class="contact">
      <p class="contact__phone">010 555 0142</p>
      <p class="contact__email">abc@copperleaf.com</p>
    </div>
  </section>
</body>
</html>
```